A-Stand Directional Sign Design

Objective:
We need a professional graphic design for an A-Stand sign that will guide customers arriving in our parking lot to our office. The design should be visually clear, welcoming, and aligned with our brand identity.
REQUIREMENTS:
Two versions of the design:
- One with an arrow pointing left
- One with an arrow pointing right
(This allows us to place the A-Stand anywhere and flip the graphic as needed.)
DIMENSIONS:
- Viewable Area: 30" x 40"
BRAND ALIGNMENT:
- Colors, fonts, and overall style should match our website: www.skornabel.com
- Clean, modern, and professional look consistent with our aviation/tourism brand
CONTENT:
- Clear directional arrow (left or right depending on version)
- Text: “Office Entrance” or similar concise wording (designers may propose alternatives if they improve clarity)
READABILITY:
- Bold, high-contrast design for visibility from a distance
- Simple layout that avoids clutter
DELIVERABLES:
- Final artwork in print-ready format (PDF preferred)
- Two versions: Arrow Left and Arrow Right
DESIGN GOAL:
Ensure customers can easily find our office upon arrival, while reinforcing skorNABEL’s professional and welcoming brand image.
Target Market(s)
Tourism

```html
<!DOCTYPE html>
<html lang="en">
<head>
<meta charset="utf-8">
<title>skorNABEL – Office Entrance A-Stand Sign</title>
<link href="https://fonts.googleapis.com/css2?family=Poppins:wght@500;600&display=swap" rel="stylesheet">
<style>
  :root {
    --stage: #7a7a7a;
    --white: #ffffff;
    --ink: #111111;
    --sky-light: #9fc3e6;
    --sky: #2f73b8;
    --navy: #0b1e3d;
    --night: #05070d;
    --cabin: #cdbfb2;
    --warm: #c9926f;
  }
  * { margin: 0; padding: 0; box-sizing: border-box; }
  html, body {
    width: 1200px; height: 1200px; overflow: hidden;
    background: var(--stage);
    font-family: "Poppins", sans-serif;
  }
  .sign {
    position: absolute; left: 0; top: 150px;
    width: 1200px; height: 900px; overflow: hidden;
  }
  .sign__photo {
    position: absolute; inset: 0;
    background:
      linear-gradient(180deg, rgba(205,191,178,0.95) 0%, rgba(205,191,178,0) 28%),
      linear-gradient(180deg, rgba(5,7,13,0) 55%, rgba(5,7,13,0.85) 100%),
      linear-gradient(90deg, var(--warm) 0%, #6d5a55 18%, var(--navy) 38%, var(--sky) 62%, var(--sky-light) 78%, #3f6f9e 100%);
  }
  .brand {
    position: absolute; left: 280px; top: 340px; width: 254px; height: 120px;
    color: var(--white);
  }
  .brand__mark {
    position: absolute; left: 118px; top: 0;
    width: 18px; height: 18px; border-radius: 50%; background: var(--white);
  }
  .brand__name {
    position: absolute; left: 0; right: 0; top: 62px; text-align: center;
    font-weight: 600; font-size: 31px; line-height: 32px; letter-spacing: 3px;
  }
  .brand__rule {
    position: absolute; left: 0; top: 102px; width: 167px; height: 2px; background: var(--white);
  }
  .brand__url {
    position: absolute; right: 0; top: 93px;
    font-weight: 600; font-size: 17px; line-height: 18px; letter-spacing: 2px;
  }
  .headline {
    position: absolute; left: 276px; top: 492px;
    font-weight: 500; font-size: 217px; line-height: 1; letter-spacing: -3px;
    color: var(--white);
  }
  .direction {
    position: absolute; left: 281px; top: 685px; width: 884px; height: 153px;
  }
  .direction svg { position: absolute; inset: 0; }
  .direction__label {
    position: absolute; left: 34px; top: 52px;
    font-weight: 500; font-size: 51px; line-height: 51px; letter-spacing: 6px;
    color: var(--ink);
  }
</style>
</head>
<body>
  <main class="sign">
    <div class="sign__photo" role="img" aria-label="Photo of three smiling passengers wearing headsets inside a helicopter cabin, blue sea visible through the window"></div>

    <div class="brand">
      <span class="brand__mark"></span>
      <span class="brand__name">skorNABEL</span>
      <span class="brand__rule"></span>
      <span class="brand__url">.COM</span>
    </div>

    <h1 class="headline">Office</h1>

    <div class="direction">
      <svg width="884" height="153" viewBox="0 0 884 153" aria-hidden="true">
        <polygon fill="#ffffff" points="0,44 762,44 762,0 884,76 762,153 762,112 0,112"/>
      </svg>
      <span class="direction__label">Entrance</span>
    </div>
  </main>
</body>
</html>
```